Wine Label: Corvinte

The project is to create 3 wine labels. The brand name is "Corvinte"

What we need is to have 3 versions: red wine, white wine and rose.

The wine is for young and modern people, between 21 and 31 years old, so it need to be casual, modern and fun, but at the same time it needs to keep the Premiums of a good European wine.

It is from Italy.

Target Market(s)

Young adults, between 21 and 31 years old. wine lovers

Requirements
Must have
• - Modern colors (Black, silver, red, etc.)
• - Clean label
• - Clear font
• - Style
• - The brand + the type of wine (red, white or rose)
Nice to have
• - A symbol to represent the brand
Should not have
• - Many elements
• - No clear fonts
• - No funny colors

```html
<!DOCTYPE html>
<html lang="en">
<head>
<meta charset="utf-8">
<title>Corvinte Rosé Wine Label</title>
<link rel="stylesheet" href="https://fonts.googleapis.com/css2?family=Cutive&display=swap">
<style>
  :root {
    --page: #ffffff;
    --label: #231f20;
    --ink: #ffffff;
    --ink-soft: #c9c9c9;
  }
  * { margin: 0; padding: 0; box-sizing: border-box; }
  html, body {
    width: 776px;
    height: 1200px;
    overflow: hidden;
    background: var(--page);
  }
  .canvas {
    position: relative;
    width: 776px;
    height: 1200px;
  }
  .wine-label {
    position: absolute;
    left: 48px;
    top: 453px;
    width: 680px;
    height: 294px;
    background: var(--label);
    font-family: "Cutive", "Courier New", serif;
    color: var(--ink);
  }
  .label-front {
    position: absolute;
    left: 0;
    top: 0;
    width: 100%;
    height: 100%;
    text-align: center;
  }
  .brand-name {
    position: absolute;
    left: 0;
    right: 0;
    top: 58px;
    font-size: 42px;
    font-weight: 400;
    letter-spacing: 1px;
    color: var(--ink);
  }
  .brand-mark {
    position: absolute;
    left: 326px;
    top: 140px;
    width: 28px;
    height: 28px;
    border-radius: 50%;
    background: var(--ink);
  }
  .wine-type {
    position: absolute;
    left: 0;
    right: 0;
    top: 212px;
    font-size: 19px;
    color: var(--ink-soft);
    letter-spacing: 1px;
  }
  .origin {
    position: absolute;
    left: 0;
    right: 0;
    top: 252px;
    font-size: 10px;
    color: var(--ink-soft);
    letter-spacing: 2px;
  }
  .seam-lines {
    position: absolute;
    left: 0;
    top: 0;
  }
</style>
</head>
<body>
<main class="canvas">
  <section class="wine-label" aria-label="Corvinte rosé wine label">
    <svg class="seam-lines" width="680" height="294" viewBox="0 0 680 294" aria-hidden="true">
      <line x1="497.5" y1="0" x2="497.5" y2="294" stroke="#ffffff" stroke-width="2"/>
      <line x1="513.5" y1="0" x2="513.5" y2="294" stroke="#ffffff" stroke-width="2"/>
    </svg>
    <div class="label-front">
      <h1 class="brand-name">Corvinte</h1>
      <span class="brand-mark" aria-hidden="true"></span>
      <p class="wine-type">Rose</p>
      <p class="origin">Made in Italy</p>
    </div>
  </section>
</main>
</body>
</html>
```